ultra-minimalist business card

front (black background, matte):

tarik b. hosseny
writer | photographer
get@tarikhosseny.com

back (white background, matte):

a picture speaks a thousand words;
a word draws a thousand pictures.

www.tarikhosseny.com

all text should be small (white or silver - as long as it shows against the black - on the front; black or gray - as long as it shows against the white - on the back).

feel free to get creative in terms of arrangement, alignment, and font type, but remember, the overall style is minimalist, so nothing too fancy, please.

thanks.

```html
<!DOCTYPE html>
<html lang="en">
<head>
<meta charset="utf-8">
<title>tarik b. hosseny — business card</title>
<link rel="stylesheet" href="https://fonts.googleapis.com/css2?family=Arimo:wght@400;500&display=swap">
<style>
  :root {
    --stage: #2b2b2d;
    --card-black: #0b0b0b;
    --card-white: #ffffff;
    --portrait-tone: #8a8196;
    --front-text: #d6d6d6;
    --front-text-soft: #bdbdbd;
    --back-text: #111111;
    --back-text-soft: #222222;
  }
  * { box-sizing: border-box; margin: 0; padding: 0; }
  html, body {
    width: 1200px;
    height: 880px;
    overflow: hidden;
    background: var(--stage);
  }
  .stage {
    width: 1200px;
    height: 880px;
    display: flex;
    flex-direction: column;
    align-items: center;
    justify-content: center;
    gap: 40px;
    font-family: "Arimo", Arial, sans-serif;
  }
  .card {
    width: 640px;
    height: 366px;
    border-radius: 22px;
    position: relative;
    overflow: hidden;
  }
  .card--front { background: var(--card-black); }
  .card--back { background: var(--card-white); }

  .portrait {
    position: absolute;
    left: 150px;
    top: 88px;
    width: 168px;
    height: 190px;
    display: block;
  }

  .contact {
    position: absolute;
    left: 396px;
    top: 150px;
    color: var(--front-text);
    line-height: 1.3;
  }
  .contact__name {
    font-size: 17px;
    font-weight: 400;
    letter-spacing: 0.2px;
    color: var(--front-text);
  }
  .contact__line {
    font-size: 12.5px;
    color: var(--front-text-soft);
  }

  .motto {
    position: absolute;
    left: 0;
    right: 0;
    top: 150px;
    text-align: center;
    font-size: 19px;
    font-weight: 500;
    line-height: 1.15;
    color: var(--back-text);
  }
  .website {
    position: absolute;
    left: 0;
    right: 0;
    top: 256px;
    text-align: center;
    font-size: 14px;
    color: var(--back-text-soft);
    letter-spacing: 0.2px;
  }
</style>
</head>
<body>
  <main class="stage">
    <section class="card card--front" aria-label="card front">
      <svg class="portrait" viewBox="0 0 168 190" role="img" aria-label="Portrait of the card owner in an oval frame">
        <ellipse cx="84" cy="95" rx="84" ry="95" fill="var(--portrait-tone)"/>
      </svg>
      <div class="contact">
        <p class="contact__name">tarik b. hosseny</p>
        <p class="contact__line">writer | photographer</p>
        <p class="contact__line">E: get@tarikhosseny.com</p>
      </div>
    </section>

    <section class="card card--back" aria-label="card back">
      <p class="motto">a picture speaks a thousand words.<br>a word draws a thousand pictures.</p>
      <p class="website">www.tarikhosseny.com</p>
    </section>
  </main>
</body>
</html>
```